Tidewell Recovery Business Card Design

Professional and clean design. The design colors should flow with the logo. Two-sided card with the website on the back which is:

www.TidewellRecovery.example.

"Specializing in Water Damage Restoration"

On the front I need the name, email, phone, and logo.

Name: Dorian Vashti
Email: Dorian@TidewellRecovery.example
Phone: 555-318-2046 for now

I only have the Preview and Thumbnail right now but should have the source files uploaded within a day or two.

Target Market(s)

Flood victims, home owners with water damage from busted pipes etc...

Industry/Entity Type

Business

Contact Information for Business Card

Name: Dorian Vashti

Font styles to use
Serif
Sans Serif

```html
<!DOCTYPE html>
<html lang="en">
<head>
<meta charset="utf-8">
<title>Tidewell Recovery Business Card</title>
<link href="https://fonts.googleapis.com/css2?family=Cinzel:wght@400;600&family=Open+Sans:wght@400&display=swap" rel="stylesheet">
<style>
  :root {
    --bg: #e9ebee;
    --card: #ffffff;
    --sky: #5bbfee;
    --brand: #2a93d5;
    --pale: #d6ecf8;
    --ink: #222a33;
    --muted: #8a8f96;
  }
  * { margin: 0; padding: 0; box-sizing: border-box; }
  html, body { width: 1200px; height: 1120px; overflow: hidden; background: var(--bg); }
  .sheet {
    width: 1200px; height: 1120px;
    display: flex; flex-direction: column; align-items: center; justify-content: center; gap: 40px;
  }
  .card {
    position: relative; width: 900px; height: 514px; background: var(--card);
    box-shadow: 0 6px 18px rgba(0,0,0,.12); overflow: hidden;
  }
  /* back side */
  .back-mark {
    position: absolute; left: 50%; top: 50%; width: 330px; height: 330px; border-radius: 50%;
    background: var(--pale); transform: translate(-50%, -50%);
  }
  .back-name {
    position: absolute; left: 0; right: 0; top: 50%; transform: translateY(-50%);
    text-align: center; font-family: "Cinzel", serif; font-weight: 600; font-size: 64px;
    letter-spacing: 2px; color: var(--brand);
  }
  /* front side */
  .band { position: absolute; left: 0; right: 0; top: 0; height: 118px; background: var(--sky); }
  .band-rule { position: absolute; left: 0; right: 0; top: 128px; height: 4px; background: var(--sky); }
  .badge {
    position: absolute; left: 50%; top: 48px; width: 120px; height: 120px; margin-left: -60px;
    border-radius: 50%; background: var(--card); border: 6px solid var(--sky);
  }
  .front-name {
    position: absolute; left: 0; right: 0; top: 196px; text-align: center;
    font-family: "Cinzel", serif; font-weight: 600; font-size: 48px; letter-spacing: 2px; color: var(--brand);
  }
  .tagline {
    position: absolute; left: 0; right: 0; top: 282px; text-align: center;
    font-family: "Cinzel", serif; font-size: 22px; letter-spacing: 1.5px; color: var(--brand);
  }
  .person { position: absolute; right: 490px; top: 380px; text-align: right; }
  .person-name { font-family: "Cinzel", serif; font-weight: 600; font-size: 30px; color: var(--brand); }
  .person-title { font-family: "Cinzel", serif; font-size: 22px; color: var(--ink); letter-spacing: 1px; margin-top: 4px; }
  .divider { position: absolute; left: 432px; top: 352px; width: 2px; height: 118px; background: #c9ccd0; }
  .contacts { position: absolute; left: 456px; top: 352px; list-style: none; }
  .contacts li {
    display: flex; align-items: center; gap: 12px; height: 39px;
    font-family: "Open Sans", sans-serif; font-size: 19px; color: var(--ink);
  }
  .contacts svg { width: 20px; height: 20px; flex: none; }
</style>
</head>
<body>
<main class="sheet">
  <section class="card card-back" aria-label="Card back">
    <div class="back-mark"></div>
    <div class="back-name">TIDEWELL RECOVERY</div>
  </section>

  <section class="card card-front" aria-label="Card front">
    <div class="band"></div>
    <div class="band-rule"></div>
    <div class="badge"></div>
    <div class="front-name">TIDEWELL RECOVERY</div>
    <p class="tagline">Specializing in Water Damage Restoration</p>
    <div class="person">
      <div class="person-name">Dorian Vashti</div>
      <div class="person-title">Title</div>
    </div>
    <div class="divider"></div>
    <ul class="contacts">
      <li>
        <svg viewBox="0 0 20 20"><circle cx="10" cy="10" r="10" fill="#2a93d5"/><path d="M7 5.5l2 2-1 1.3c.6 1.3 1.5 2.2 2.8 2.8l1.2-1 2 2-1.3 1.6c-3.3-.3-6.6-3.6-6.9-6.9z" fill="#fff"/></svg>
        555-318-2046
      </li>
      <li>
        <svg viewBox="0 0 20 20"><circle cx="10" cy="10" r="10" fill="#2a93d5"/><rect x="5" y="6.5" width="10" height="7" fill="#fff"/><path d="M5 6.5l5 4 5-4" fill="none" stroke="#2a93d5" stroke-width="1"/></svg>
        Dorian@TidewellRecovery.example
      </li>
      <li>
        <svg viewBox="0 0 20 20"><circle cx="10" cy="10" r="10" fill="#2a93d5"/><g fill="none" stroke="#fff" stroke-width="1"><circle cx="10" cy="10" r="5.5"/><ellipse cx="10" cy="10" rx="2.4" ry="5.5"/><path d="M4.5 10h11"/></g></svg>
        www.TidewellRecovery.example
      </li>
    </ul>
  </section>
</main>
</body>
</html>
```